Fitness Business Card Design Needed

We are looking for a business card design that stands out but is also simple and unique. I like the idea of on one side using the picture of myself with my logo at my feet. I love the texture on the business card so please take that into account when designing. Then on the other side having my contact details. I want it to be clean, modern, and pretty. I am open to designs that allow spot gloss or gold foiling.

Contact Information for Business Card

Space for Name, Phone number, email, and website

```html
<!DOCTYPE html>
<html lang="en">
<head>
<meta charset="utf-8">
<title>Halden Coaching – Business Card</title>
<link rel="stylesheet" href="https://fonts.googleapis.com/css2?family=Open+Sans:wght@400;600&display=swap">
<style>
  :root {
    --page-bg: #ecebe8;
    --card-white: #f4f4f3;
    --ink: #2b2b2b;
    --ink-soft: #4a4a4a;
    --gold: #d9a94f;
    --gold-light: #f0cf83;
    --gold-deep: #b98a36;
    --gold-text: #e0a948;
    --photo-tone: #c99f82;
  }
  * { box-sizing: border-box; margin: 0; padding: 0; }
  html, body { width: 1200px; height: 1200px; overflow: hidden; }
  body {
    background: var(--page-bg);
    font-family: "Open Sans", sans-serif;
    color: var(--ink);
    position: relative;
  }
  .card {
    position: absolute;
    left: 250px;
    width: 700px;
    height: 400px;
    box-shadow: 0 6px 22px rgba(0,0,0,0.14);
    overflow: hidden;
  }

  /* Photo side */
  .card--photo {
    top: 170px;
    background: linear-gradient(120deg, var(--gold-deep) 0%, var(--gold) 35%, var(--gold-light) 60%, var(--gold) 100%);
  }
  .portrait {
    position: absolute;
    left: 40px;
    top: 0;
    width: 340px;
    height: 400px;
    background: linear-gradient(180deg, rgba(201,159,130,0.55) 0%, var(--photo-tone) 55%, rgba(201,159,130,0.35) 100%);
  }

  /* Brand name: plain text with one square */
  .brand {
    position: absolute;
    display: flex;
    align-items: center;
    gap: 14px;
  }
  .brand-square {
    width: 26px;
    height: 26px;
    border: 2px solid currentColor;
    flex: none;
  }
  .brand-name {
    font-family: "Open Sans", sans-serif;
    font-weight: 600;
    font-size: 24px;
    white-space: nowrap;
  }
  .card--photo .brand { right: 56px; top: 180px; color: var(--ink); }

  /* Contact side */
  .card--contact {
    top: 630px;
    background: var(--card-white);
  }
  .card--contact .brand { left: 60px; top: 162px; color: var(--ink); }
  .card--contact .brand-square { border-color: var(--gold); }
  .divider {
    position: absolute;
    left: 340px;
    top: 110px;
    width: 1px;
    height: 170px;
    background: var(--ink-soft);
  }
  .details {
    position: absolute;
    left: 372px;
    top: 108px;
  }
  .person-name {
    font-size: 24px;
    font-weight: 400;
    color: var(--gold-text);
    line-height: 1.1;
  }
  .person-role {
    font-size: 12px;
    color: var(--ink-soft);
    margin: 4px 0 16px;
  }
  .contact-list { list-style: none; font-size: 13px; line-height: 1.55; color: var(--ink); }
  .contact-list li { display: flex; align-items: flex-start; gap: 10px; }
  .contact-list svg { width: 13px; height: 13px; margin-top: 3px; flex: none; fill: var(--ink); }
  .contact-list .address { margin-bottom: 8px; }
  .gold-band {
    position: absolute;
    left: 320px;
    right: 0;
    bottom: 0;
    height: 22px;
    background: linear-gradient(100deg, var(--gold-deep), var(--gold-light) 45%, var(--gold) 100%);
  }
</style>
</head>
<body>

<section class="card card--photo">
  <div class="portrait" role="img" aria-label="Photograph of the trainer in athletic wear"></div>
  <div class="brand">
    <span class="brand-square"></span>
    <span class="brand-name">Halden Coaching</span>
  </div>
</section>

<section class="card card--contact">
  <div class="brand">
    <span class="brand-square"></span>
    <span class="brand-name">Halden Coaching</span>
  </div>
  <div class="divider"></div>
  <div class="details">
    <h1 class="person-name">Lena R. Hollis</h1>
    <p class="person-role">Trainer</p>
    <ul class="contact-list">
      <li class="address">
        <svg viewBox="0 0 24 24"><path d="M12 2a7 7 0 0 0-7 7c0 5 7 13 7 13s7-8 7-13a7 7 0 0 0-7-7zm0 9.5A2.5 2.5 0 1 1 12 6.5a2.5 2.5 0 0 1 0 5z"/></svg>
        <span>Brightwater<br>Ashford County</span>
      </li>
      <li>
        <svg viewBox="0 0 24 24"><path d="M6.6 10.8a15 15 0 0 0 6.6 6.6l2.2-2.2c.3-.3.7-.4 1-.2 1.1.4 2.3.6 3.6.6.6 0 1 .4 1 1V20c0 .6-.4 1-1 1A17 17 0 0 1 3 4c0-.6.4-1 1-1h3.5c.6 0 1 .4 1 1 0 1.3.2 2.5.6 3.6.1.3 0 .7-.2 1z"/></svg>
        <span>555-0187-2241</span>
      </li>
      <li>
        <svg viewBox="0 0 24 24"><path d="M2 5h20v14H2zm2 2v.5l8 5 8-5V7l-8 5z"/></svg>
        <span>lena@haldencoaching.com</span>
      </li>
      <li>
        <svg viewBox="0 0 24 24"><path d="M12 2a10 10 0 1 0 0 20 10 10 0 0 0 0-20zm6.9 9h-3a15 15 0 0 0-1.4-6A8 8 0 0 1 18.9 11zM12 4c1 1.3 1.8 3.9 1.9 7h-3.8C10.2 7.9 11 5.3 12 4zM9.5 5a15 15 0 0 0-1.4 6h-3A8 8 0 0 1 9.5 5zM5.1 13h3a15 15 0 0 0 1.4 6A8 8 0 0 1 5.1 13zM12 20c-1-1.3-1.8-3.9-1.9-7h3.8c-.1 3.1-.9 5.7-1.9 7zm2.5-1a15 15 0 0 0 1.4-6h3a8 8 0 0 1-4.4 6z"/></svg>
        <span>www.haldencoaching.com</span>
      </li>
    </ul>
  </div>
  <div class="gold-band"></div>
</section>

</body>
</html>
```